Local Electrical company need some kick ass business cards

In need of some in your face design business cards for a family owned electrical service company in Edmonton, Alberta Canada. We provide reliable and trustworthy electrical service for commercial and residential work in the Edmonton and area. We have been in business for 25 years.

Target Market(s)

Residential and commercial electrical

Industry/Entity Type

Business

Contact Information for Business Card

Your welcome to change and modify the brightway electric logo. please include the lightbulb! Our Colours are black and green please stay with that.
Please include a name phone number and address on the card
phone number - 780-318-5062
#22, 418 Maple Cres, St.Albert, Alberta.
Two things that need to be on the card.
"your friendly neighborhood electrictrician"
Commercial & residential electrical repair and service

Colors
9bcb3c

Requirements
Must have
• Light bulb guy Attached
• "your friendly neighborhood electrictrician"
• Commercial & residential electrical repair and service
• phone number - 780-318-5062
• #22, 418 Maple Cres, St.Albert, Alberta.
• Our colours are black and green
Nice to have
• go wild i want something loud

```html
<!DOCTYPE html>
<html lang="en">
<head>
<meta charset="utf-8">
<title>Brightway Electric — Business Card</title>
<link rel="stylesheet" href="https://fonts.googleapis.com/css2?family=Source+Sans+3:wght@400;600;700&display=swap">
<style>
  :root {
    --stage: #161616;
    --card-white: #ffffff;
    --brand-green: #6abf45;
    --accent-green: #7dc242;
    --ink: #333333;
    --ink-dark: #111111;
    --ghost: #f1f2f0;
    --mascot-light: #e9f2e2;
  }
  * { margin: 0; padding: 0; box-sizing: border-box; }
  html, body {
    width: 1200px; height: 900px; overflow: hidden;
    background: var(--stage);
    font-family: "Source Sans 3", sans-serif;
  }
  .card {
    position: absolute;
    top: 305px;
    width: 444px; height: 258px;
    border-radius: 10px;
    overflow: hidden;
  }
  .card-front { left: 147px; background: var(--card-white); }
  .card-back { left: 631px; background: var(--brand-green); color: #fff; text-align: center; }

  .mascot-ghost {
    position: absolute; left: 272px; top: 0; width: 172px; height: 258px;
    background: radial-gradient(ellipse at 55% 40%, var(--ghost) 0%, #f7f7f6 60%, rgba(255,255,255,0) 100%);
  }
  .wordmark {
    position: absolute; left: 36px; top: 117px;
    display: flex; align-items: center; gap: 8px;
  }
  .wordmark-dot { width: 14px; height: 14px; border-radius: 50%; background: var(--accent-green); }
  .wordmark-name {
    font-weight: 700; font-size: 22px; color: var(--ink-dark); letter-spacing: 0.5px;
  }
  .contact { position: absolute; left: 236px; top: 48px; color: var(--ink); font-size: 13px; line-height: 16px; }
  .contact-name { color: var(--accent-green); font-weight: 600; font-size: 19px; line-height: 22px; }
  .contact-role { margin-bottom: 12px; }
  .contact-address { margin-bottom: 13px; }
  .contact-list { list-style: none; }
  .contact-list li { display: flex; align-items: center; gap: 8px; height: 17px; }
  .contact-list svg { width: 10px; height: 10px; fill: var(--accent-green); flex: none; }

  .tagline { position: absolute; left: 0; right: 0; top: 27px; font-size: 23px; font-weight: 600; line-height: 30px; }
  .mascot {
    position: absolute; left: 199px; top: 90px; width: 54px; height: 88px;
    border-radius: 26px 26px 10px 10px;
    background: linear-gradient(180deg, var(--mascot-light) 0%, #d9ded6 70%, #9aa09a 100%);
  }
  .services { position: absolute; left: 0; right: 0; top: 184px; font-size: 20px; font-weight: 600; line-height: 26px; }
</style>
</head>
<body>
  <section class="card card-front">
    <div class="mascot-ghost" role="img" aria-label="Faint light bulb mascot wearing a cap"></div>
    <div class="wordmark">
      <span class="wordmark-dot"></span>
      <span class="wordmark-name">Brightway Electric</span>
    </div>
    <div class="contact">
      <p class="contact-name">Daniel Reeves</p>
      <p class="contact-role">Managing Director</p>
      <p class="contact-address">#22, 418 Maple Cres,<br>St.Albert, Alberta.</p>
      <ul class="contact-list">
        <li><svg viewBox="0 0 10 10"><rect x="2" y="0" width="6" height="10" rx="1"/></svg>780-318-5062</li>
        <li><svg viewBox="0 0 10 10"><path d="M0 4 Q5 0 10 4 L8 6 L6 5 L4 5 L2 6 Z M2 7 H8 V10 H2 Z"/></svg>780-318-5062</li>
        <li><svg viewBox="0 0 10 10"><rect x="0" y="3" width="10" height="7"/><rect x="2" y="0" width="6" height="3"/></svg>780-318-5062</li>
        <li><svg viewBox="0 0 10 10"><path d="M0 2 H10 V9 H0 Z" /></svg>info@youremail.com</li>
        <li><svg viewBox="0 0 10 10"><path d="M1 9 L4 6 L5 7 L2 10 Z M6 1 L9 4 L8 5 L5 2 Z M3 7 L7 3 L7.6 3.6 L3.6 7.6 Z"/></svg>www.yourweb.com</li>
      </ul>
    </div>
  </section>

  <section class="card card-back">
    <h2 class="tagline">Your friendly neighborhood<br>electrictrician</h2>
    <div class="mascot" role="img" aria-label="Light bulb mascot in a green cap"></div>
    <p class="services">Commercial &amp; Residential<br>Electrical Repair and Service</p>
  </section>
</body>
</html>
```